I need a business card design for: Brennle Financial Solutions. Logo design has been attached. I will also need the business address: 418 West Larkin Rd. Suite 310C Harwick Falls, HF 00418. Phone and Fax : 555-218-4903 (phone) and 555-218-4907 (fax). Email address: tbrennle@brennlefinancialsolutions.example. Please add my title: Financial Advisor.
The following disclosure must appear on business card, letterhead, and stationary: Securities and investment advisory services offered through Delmont Equities Corporation (DEC) member QUALTA/RVOB. DEC is separately owned and other entities and/or marketing names, products or services referenced here are independent of DEC.

```html
<!DOCTYPE html>
<html lang="en">
<head>
<meta charset="utf-8">
<title>Brennle Financial Solutions – Business Card</title>
<link rel="stylesheet" href="https://fonts.googleapis.com/css2?family=Roboto:wght@400;500;700&display=swap">
<style>
  :root {
    --page-bg: #d3d6d8;
    --card-white: #f1f1ef;
    --navy: #172d5c;
    --navy-deep: #13264f;
    --ink: #2b2f36;
    --paper-text: #e9ecf2;
  }
  * { box-sizing: border-box; margin: 0; padding: 0; }
  html, body {
    width: 1200px; height: 1050px; overflow: hidden;
    background: var(--page-bg);
    font-family: "Roboto", Arial, sans-serif;
  }
  .sheet {
    width: 1200px; height: 1050px;
    display: flex; flex-direction: column; align-items: center; justify-content: center;
    gap: 30px;
  }
  .card {
    width: 840px; height: 480px;
    position: relative;
    box-shadow: 0 6px 18px rgba(0,0,0,0.12);
  }

  /* Front */
  .card--front { background: var(--card-white); color: var(--ink); }
  .contact { position: absolute; left: 60px; top: 92px; width: 420px; }
  .contact__name {
    font-weight: 700; font-size: 26px; letter-spacing: 0.5px;
    color: var(--navy); text-transform: uppercase;
  }
  .contact__title { font-size: 22px; margin-top: 2px; margin-bottom: 16px; }
  .contact__line { font-size: 18px; line-height: 1.35; }
  .contact__row { display: flex; align-items: center; gap: 8px; font-size: 18px; line-height: 1.4; white-space: nowrap; }
  .contact__row svg { width: 17px; height: 17px; fill: var(--navy); flex: none; }

  .brand { position: absolute; display: flex; align-items: center; gap: 14px; }
  .brand__dot { border-radius: 50%; flex: none; }
  .brand__name { font-weight: 500; text-transform: uppercase; line-height: 1.05; white-space: nowrap; }
  .card--front .brand { right: 60px; top: 200px; }
  .card--front .brand__dot { width: 46px; height: 46px; background: var(--navy); }
  .card--front .brand__name { color: var(--navy); font-size: 26px; }
  .brand__rule { display: block; height: 2px; background: currentColor; margin-top: 8px; }

  /* Back */
  .card--back { background: var(--navy-deep); color: var(--paper-text); }
  .card--back .brand { left: 50%; transform: translateX(-50%); top: 100px; }
  .card--back .brand__dot { width: 64px; height: 64px; background: var(--paper-text); }
  .card--back .brand__name { font-size: 36px; color: var(--paper-text); }
  .disclosure {
    position: absolute; left: 70px; right: 70px; top: 240px;
    font-size: 19px; line-height: 1.45; text-align: center;
  }
</style>
</head>
<body>
<main class="sheet">

  <section class="card card--front" aria-label="Business card front">
    <div class="contact">
      <p class="contact__name">Tobias Brennle</p>
      <p class="contact__title">Financial Advisor</p>
      <p class="contact__line">Brennle Financial Solutions</p>
      <p class="contact__line">418 West Larkin Rd. Suite 310C</p>
      <p class="contact__line">Harwick Falls, HF 00418</p>
      <p class="contact__row">
        <svg viewBox="0 0 24 24" aria-hidden="true"><path d="M6.6 10.8a15.1 15.1 0 0 0 6.6 6.6l2.2-2.2c.3-.3.7-.4 1-.2 1.1.4 2.3.6 3.6.6.6 0 1 .4 1 1V20c0 .6-.4 1-1 1A17 17 0 0 1 3 4c0-.6.4-1 1-1h3.5c.6 0 1 .4 1 1 0 1.3.2 2.5.6 3.6.1.3 0 .7-.2 1z"/></svg>
        <span>555-218-4903</span>
      </p>
      <p class="contact__row">
        <svg viewBox="0 0 24 24" aria-hidden="true"><path d="M7 3h10v5H7zM4 9h16a2 2 0 0 1 2 2v6h-4v4H6v-4H2v-6a2 2 0 0 1 2-2zm4 7v3h8v-3z"/></svg>
        <span>555-218-4907</span>
      </p>
      <p class="contact__row">
        <svg viewBox="0 0 24 24" aria-hidden="true"><path d="M2 5h20v14H2zm2 2v.5l8 5 8-5V7z"/></svg>
        <span>tbrennle@brennlefinancialsolutions.example</span>
      </p>
    </div>

    <div class="brand">
      <span class="brand__dot" aria-hidden="true"></span>
      <p class="brand__name">Brennle Financial<br>Solutions<span class="brand__rule" aria-hidden="true"></span></p>
    </div>
  </section>

  <section class="card card--back" aria-label="Business card back">
    <div class="brand">
      <span class="brand__dot" aria-hidden="true"></span>
      <p class="brand__name">Brennle Financial<br>Solutions<span class="brand__rule" aria-hidden="true"></span></p>
    </div>
    <p class="disclosure">Securities and investment advisory services offered through Delmont Equities Corporation (DEC) member QUALTA/RVOB. DEC is separately owned and other entities and/or marketing names, products or services referenced here are independent of DEC.</p>
  </section>

</main>
</body>
</html>
```